Brightwell Mechanical - Business Card Design

We would like a dark (likely black) themed business card to be able to hand out to potential clients. We may list our services on the card or keep it clean. Unsure. Logo attached

```html
<!DOCTYPE html>
<html lang="en">
<head>
<meta charset="utf-8">
<title>Brightwell Mechanical – Business Cards</title>
<link href="https://fonts.googleapis.com/css2?family=Lato:wght@400;700;900&display=swap" rel="stylesheet">
<style>
  :root {
    --stage: #2b2622;
    --card: #050505;
    --orange: #f15a22;
    --blue: #2a7fd4;
    --white: #ffffff;
  }
  * { box-sizing: border-box; margin: 0; padding: 0; }
  html, body { width: 1200px; height: 847px; overflow: hidden; }
  body {
    background: var(--stage);
    font-family: "Lato", sans-serif;
    position: relative;
  }
  .card {
    position: absolute;
    width: 540px;
    height: 309px;
    background: var(--card);
    border: 3px solid var(--orange);
    overflow: hidden;
  }
  .card--front { left: 50px; top: 140px; }
  .card--back { left: 610px; top: 398px; }

  .brand {
    display: flex;
    align-items: center;
    gap: 10px;
  }
  .brand__dot {
    width: 22px; height: 22px;
    border-radius: 50%;
    background: var(--orange);
    flex: none;
  }
  .brand__name {
    color: var(--blue);
    font-weight: 900;
    font-size: 26px;
    letter-spacing: 0.5px;
    text-transform: uppercase;
    line-height: 1.05;
  }

  .card--front .brand {
    position: absolute;
    left: 0; right: 0; top: 92px;
    justify-content: center;
  }
  .services {
    position: absolute;
    left: 0; right: 0; top: 206px;
    height: 32px;
    background: var(--blue);
    color: var(--white);
    font-size: 15px;
    letter-spacing: 1.2px;
    display: flex;
    align-items: center;
    justify-content: center;
    text-transform: uppercase;
  }

  .card--back .brand {
    position: absolute;
    left: 28px; top: 118px;
    width: 250px;
  }
  .card--back .brand__name { font-size: 22px; }
  .divider {
    position: absolute;
    left: 292px; top: 70px;
    width: 2px; height: 165px;
    background: var(--orange);
  }
  .contact {
    position: absolute;
    left: 316px; top: 72px;
    color: var(--blue);
    font-size: 14px;
    line-height: 1.45;
  }
  .contact__name {
    color: var(--orange);
    font-weight: 900;
    font-size: 26px;
    line-height: 1.1;
    text-transform: uppercase;
  }
  .contact__role { margin-bottom: 6px; }
  .contact__row { display: flex; align-items: center; gap: 8px; }
  .contact__row svg { width: 13px; height: 13px; flex: none; }
</style>
</head>
<body>

<section class="card card--front" aria-label="Card front">
  <div class="brand">
    <span class="brand__dot"></span>
    <span class="brand__name">Brightwell Mechanical</span>
  </div>
  <div class="services">HVAC &nbsp;|&nbsp; Plumbing &nbsp;|&nbsp; Boiler &nbsp;|&nbsp; Heating and Air</div>
</section>

<section class="card card--back" aria-label="Card back">
  <div class="brand">
    <span class="brand__dot"></span>
    <span class="brand__name">Brightwell Mechanical</span>
  </div>
  <div class="divider"></div>
  <div class="contact">
    <p class="contact__name">John Smith</p>
    <p class="contact__role">Founder &amp; CEO</p>
    <p>1234 First Line Address</p>
    <p>5678 Second Line Address</p>
    <p class="contact__row">
      <svg viewBox="0 0 16 16" aria-hidden="true"><path fill="var(--orange)" d="M3.6 1.5l2.3 2.6-1.3 1.7c.9 2 2.5 3.6 4.6 4.6l1.7-1.3 2.6 2.3-1.5 2.1C6.9 13.4 2.6 9.1 1.5 3z"/></svg>
      1234567890
    </p>
    <p class="contact__row">
      <svg viewBox="0 0 16 16" aria-hidden="true"><rect x="1" y="3" width="14" height="10" fill="var(--orange)"/><path d="M1.5 3.5L8 9l6.5-5.5" stroke="var(--card)" stroke-width="1.4" fill="none"/></svg>
      info@yourmail.com
    </p>
    <p class="contact__row">
      <svg viewBox="0 0 16 16" aria-hidden="true"><circle cx="8" cy="8" r="6.5" fill="none" stroke="var(--orange)" stroke-width="1.5"/><ellipse cx="8" cy="8" rx="2.8" ry="6.5" fill="none" stroke="var(--orange)" stroke-width="1.2"/><path d="M1.5 8h13" stroke="var(--orange)" stroke-width="1.2"/></svg>
      www.yourwebsite.com
    </p>
  </div>
</section>

</body>
</html>
```